Request for Business Card Design

Hi. My name is Marlena, I am looking for a new business card design for my company, Quillbrook Sensing Systems, LLC. I really like the design you did for Tavel Harvest and was hoping you could do something similar using our full logo and our mark. I am also open to any raised texture design using our mark. I have attached our full logo, which would need to be somewhere on the card, as well as the mark in both outline and full form, as well as our brand colors / guide. The card does not have to be white, as long as our logo and mark appear. I actually like darker colored business cards more, but am open to all options. If you are interested in working with me, please let me know. We would also take the business card design into letterhead design if you can do that.

```html
<!DOCTYPE html>
<html lang="en">
<head>
<meta charset="utf-8">
<title>Quillbrook Sensing Systems – Business Card</title>
<link href="https://fonts.googleapis.com/css2?family=Open+Sans:wght@400;600;700&display=swap" rel="stylesheet">
<style>
  :root {
    --backdrop: #3a3a3a;
    --card: #151515;
    --accent: #1a9fd6;
    --text: #f2f2f2;
    --emboss: #2a2a2a;
  }
  * { margin: 0; padding: 0; box-sizing: border-box; }
  html, body { width: 1200px; height: 801px; overflow: hidden; }
  body {
    background: var(--backdrop);
    font-family: "Open Sans", Arial, sans-serif;
    position: relative;
  }
  .card {
    position: absolute;
    top: 246px;
    width: 540px;
    height: 309px;
    background: var(--card);
    border-bottom: 3px solid var(--accent);
    box-shadow: 0 10px 30px rgba(0,0,0,.45);
  }
  .card--front { left: 40px; }
  .card--back { left: 620px; }

  .brand {
    position: absolute;
    display: flex;
    align-items: center;
    gap: 12px;
  }
  .brand__dot {
    width: 34px; height: 34px;
    border-radius: 50%;
    background: var(--accent);
  }
  .brand__name {
    font-weight: 700;
    color: var(--text);
    letter-spacing: .06em;
    line-height: 1.15;
    font-size: 17px;
    text-transform: uppercase;
  }
  .card--front .brand { left: 200px; top: 44px; }

  .rule {
    position: absolute;
    height: 1px;
    background: var(--accent);
  }
  .rule--main { left: 150px; right: 28px; top: 122px; }
  .rule--contact { left: 30px; width: 250px; top: 222px; }

  .address {
    position: absolute;
    right: 34px; top: 138px;
    text-align: right;
    color: var(--text);
    font-size: 12.5px;
    line-height: 1.5;
  }
  .person { position: absolute; left: 30px; top: 168px; }
  .person__name {
    color: var(--accent);
    font-weight: 700;
    font-size: 19px;
    letter-spacing: .03em;
    text-transform: uppercase;
  }
  .person__title { color: var(--text); font-size: 13px; }

  .contacts {
    position: absolute; left: 30px; top: 232px;
    list-style: none;
    color: var(--text);
    font-size: 12.5px;
    line-height: 1.55;
  }
  .contacts li { display: flex; align-items: center; gap: 10px; }
  .contacts svg { width: 11px; height: 11px; fill: var(--accent); flex: none; }

  .card--back .brand { left: 100px; top: 122px; gap: 18px; }
  .card--back .brand__dot { width: 56px; height: 56px; background: var(--emboss); }
  .card--back .brand__name { color: var(--emboss); font-size: 26px; }
</style>
</head>
<body>
  <section class="card card--front">
    <div class="brand">
      <span class="brand__dot"></span>
      <span class="brand__name">Quillbrook<br>Sensing Systems</span>
    </div>
    <div class="rule rule--main"></div>
    <p class="address">4172 Harbor Reach Dr<br>Calloway Bay CA 90000</p>
    <div class="person">
      <p class="person__name">Dorian Vell</p>
      <p class="person__title">President</p>
    </div>
    <div class="rule rule--contact"></div>
    <ul class="contacts">
      <li><svg viewBox="0 0 24 24"><path d="M6.6 10.8a15.1 15.1 0 0 0 6.6 6.6l2.2-2.2a1 1 0 0 1 1-.25 11.4 11.4 0 0 0 3.6.57 1 1 0 0 1 1 1V20a1 1 0 0 1-1 1A17 17 0 0 1 3 4a1 1 0 0 1 1-1h3.5a1 1 0 0 1 1 1c0 1.25.2 2.45.57 3.57a1 1 0 0 1-.25 1z"/></svg>555-013-4827</li>
      <li><svg viewBox="0 0 24 24"><path d="M2 5h20v14H2zm2 2v.5l8 5 8-5V7z"/></svg>d.vell@quillbrook.com</li>
      <li><svg viewBox="0 0 24 24"><circle cx="12" cy="12" r="10"/></svg>www.quillbrook.com</li>
    </ul>
  </section>

  <section class="card card--back">
    <div class="brand">
      <span class="brand__dot"></span>
      <span class="brand__name">Quillbrook<br>Sensing Systems</span>
    </div>
  </section>
</body>
</html>
```